Business card for Northway's Blue Wagon.

Good day i am looking for a business card design for my business.
The name of the business is Northway's Blue Wagon. It is a van rental business that provides a driver and helper to the customer. Customer have use to van for small moves, studio or 1 bedroom, Moving furniture like couch or kitchen cabinets.
We are available evenings, weekends and holidays.
the means to contact us is by phone at 614-927-3048; By emails at Kestrel@northwaysbluewagon-example.com; or by social media, Facebook and Instagram.
You can see attached pictures of the van and or logo.

```html
<!DOCTYPE html>
<html lang="en">
<head>
<meta charset="utf-8">
<title>Northway's Blue Wagon — Business Card</title>
<link href="https://fonts.googleapis.com/css2?family=Montserrat:wght@400;600&display=swap" rel="stylesheet">
<style>
  :root {
    --backdrop: #13161a;
    --card-white: #ffffff;
    --brand-red: #c22a20;
    --ink-black: #0c0c0c;
    --text-grey: #666666;
    --rule-grey: #e2e2e2;
  }
  * { margin: 0; padding: 0; box-sizing: border-box; }
  html, body {
    width: 1200px;
    height: 1145px;
    overflow: hidden;
    background: var(--backdrop);
    font-family: "Montserrat", sans-serif;
  }
  .sheet {
    width: 1200px;
    height: 1145px;
    display: flex;
    flex-direction: column;
    align-items: center;
    justify-content: center;
    gap: 40px;
  }
  .card {
    position: relative;
    width: 900px;
    height: 514px;
    overflow: hidden;
  }
  .card-front { background: var(--card-white); }
  .card-back { background: var(--brand-red); }

  .edge-bar {
    position: absolute;
    top: 180px;
    width: 16px;
    height: 136px;
  }
  .edge-bar-left { left: 0; background: var(--brand-red); }
  .edge-bar-right { right: 0; background: var(--ink-black); }

  .brand-name {
    position: absolute;
    left: 60px;
    top: 188px;
    width: 180px;
    height: 122px;
    display: flex;
    align-items: center;
    justify-content: center;
    text-align: center;
    color: var(--brand-red);
    font-weight: 600;
    font-size: 21px;
    line-height: 1.25;
  }
  .divider {
    position: absolute;
    left: 300px;
    top: 196px;
    width: 1px;
    height: 106px;
    background: var(--rule-grey);
  }
  .contact-list {
    position: absolute;
    left: 348px;
    top: 172px;
    list-style: none;
    font-size: 19px;
    color: var(--text-grey);
    white-space: nowrap;
  }
  .contact-list li {
    display: flex;
    height: 51px;
    align-items: center;
  }
  .contact-label {
    width: 40px;
    flex: none;
    color: var(--brand-red);
  }

  .emblem-circle {
    position: absolute;
    left: 283px;
    top: 90px;
    width: 334px;
    height: 334px;
    border-radius: 50%;
    background: var(--card-white);
    display: flex;
    align-items: center;
    justify-content: center;
    text-align: center;
    color: var(--brand-red);
    font-weight: 600;
    font-size: 30px;
    line-height: 1.25;
    padding: 40px;
  }
</style>
</head>
<body>
<main class="sheet">
  <section class="card card-front" aria-label="Card front">
    <span class="edge-bar edge-bar-left"></span>
    <p class="brand-name">Northway's Blue Wagon</p>
    <span class="divider"></span>
    <ul class="contact-list">
      <li><span class="contact-label">P:</span>+1 (614)-927-3048</li>
      <li><span class="contact-label">E:</span>kestrel@northwaysbluewagon-example.com</li>
      <li><span class="contact-label">w:</span>www.northwaysbluewagon-example.com</li>
    </ul>
    <span class="edge-bar edge-bar-right"></span>
  </section>

  <section class="card card-back" aria-label="Card back">
    <p class="emblem-circle">Northway's Blue Wagon</p>
  </section>
</main>
</body>
</html>
```